My company is all about art and painting people's walls, cars and everything you can imagine, I would like a sharp professional buisness card which still has a good creative element

Industry/Entity Type

Painting

Contact Information for Business Card

Ka Tivo Art
Canvass,Murals,Vehicles,Cover art and tattoo design
Commissions available..
Www.pixelmeet.com/valdipe

```html
<!DOCTYPE html>
<html lang="en">
<head>
<meta charset="utf-8">
<title>Ka Tivo Arts – Business Card</title>
<link rel="stylesheet" href="https://fonts.googleapis.com/css2?family=PT+Sans:ital,wght@0,700;1,400&display=swap">
<style>
  :root {
    --ink: #111111;
    --brand: #1c1c1c;
    --swirl-pink: #f27fc0;
    --swirl-orange: #f6b36a;
    --swirl-yellow: #f3e98a;
    --swirl-green: #a9dca6;
    --swirl-cyan: #9fd8ec;
    --swirl-blue: #8fa6e6;
    --swirl-violet: #b58fdc;
    --swirl-red: #f08a8a;
  }
  html, body {
    margin: 0;
    padding: 0;
    overflow: hidden;
    background: #ffffff;
  }
  .card {
    position: relative;
    width: 1200px;
    height: 695px;
    overflow: hidden;
    font-family: "PT Sans", "Myriad Pro", sans-serif;
  }
  .card__backdrop {
    position: absolute;
    inset: 0;
    background:
      radial-gradient(ellipse 60% 45% at 25% 30%, rgba(242,127,192,0.85), transparent 70%),
      radial-gradient(ellipse 55% 40% at 75% 20%, rgba(243,233,138,0.8), transparent 70%),
      radial-gradient(ellipse 50% 45% at 80% 70%, rgba(181,143,220,0.85), transparent 70%),
      radial-gradient(ellipse 45% 40% at 15% 80%, rgba(240,138,138,0.75), transparent 70%),
      radial-gradient(ellipse 50% 40% at 50% 60%, rgba(159,216,236,0.85), transparent 70%),
      linear-gradient(160deg, var(--swirl-cyan) 0%, var(--swirl-orange) 20%, var(--swirl-pink) 38%, var(--swirl-green) 55%, var(--swirl-blue) 75%, var(--swirl-violet) 100%);
  }
  .brand-name {
    position: absolute;
    left: 80px;
    top: 48px;
    margin: 0;
    font-weight: 700;
    font-size: 72px;
    line-height: 1;
    color: var(--brand);
  }
  .services {
    position: absolute;
    left: 0;
    top: 282px;
    width: 1126px;
    margin: 0;
    text-align: center;
    font-style: italic;
    font-weight: 400;
    font-size: 64px;
    line-height: 56px;
    color: var(--ink);
  }
  .web-address {
    position: absolute;
    right: 24px;
    top: 628px;
    margin: 0;
    font-style: italic;
    font-weight: 400;
    font-size: 46px;
    line-height: 1;
    color: var(--ink);
  }
</style>
</head>
<body>
  <main class="card">
    <div class="card__backdrop" role="img" aria-label="Abstract rainbow swirl of soft painted brush strokes in pink, orange, yellow, green, blue and violet"></div>
    <h1 class="brand-name">Ka Tivo Arts</h1>
    <p class="services">Canvass,Murals,Vehicles,Cover art<br>&amp; tattoo design Commissions<br>available</p>
    <p class="web-address">Www.pixelmeet.com/valdipe</p>
  </main>
</body>
</html>
```